Business card for real estate agent / office

We're looking for a new business card. We want something that is pretty clean, modern and sleek. Something that also tells people that we are a new age company...cutting edge. Although real estate has been done a certain way the last 100 years, we have energy and vibrance. Company name is Silver Meadow Properties. info can be found here: http://www.smprealtyhub.example/

needs to include: Name, title, phone number, email. our license number also needs to be displayed somewhere.

Target Market(s)

25-55 homeowners or potential homeowners

Industry/Entity Type

Business

Contact Information for Business Card

we need business card designs for real estate agent / office

Font styles to use
Serif

Requirements
Must have
• needs to include: Name, title, phone number, email. our license number also needs to be displayed somewhere and company name.
Nice to have
• placement area for photo

```html
<!DOCTYPE html>
<html lang="en">
<head>
<meta charset="utf-8">
<title>Silver Meadow Properties – Business Cards</title>
<link rel="stylesheet" href="https://fonts.googleapis.com/css2?family=Spectral:ital,wght@0,400;0,600;1,400&display=swap">
<style>
  :root {
    --page: #ffffff;
    --navy: #052845;
    --copper: #c27a45;
    --green: #5cb845;
    --brand-blue: #1a4f7a;
    --ink: #4a4a4a;
    --muted: #6b6b6b;
    --photo-top: #3f6b35;
    --photo-bottom: #1f3552;
  }
  * { box-sizing: border-box; margin: 0; padding: 0; }
  html, body { width: 1200px; height: 1000px; overflow: hidden; background: var(--page); }
  body { position: relative; font-family: "Spectral", Georgia, serif; }

  .card {
    position: absolute;
    width: 426px;
    height: 260px;
    box-shadow: 0 2px 6px rgba(0,0,0,0.28);
  }
  .card--front { background: var(--navy); top: 225px; display: flex; align-items: center; justify-content: center; }
  .card--back { background: #fff; top: 516px; }
  .card--left { left: 134px; }
  .card--right { left: 640px; }

  .wordmark { display: flex; align-items: center; gap: 10px; font-weight: 600; white-space: nowrap; }
  .wordmark__square { display: block; flex: none; }
  .wordmark--front { color: var(--copper); font-size: 25px; }
  .wordmark--front .wordmark__square { width: 22px; height: 22px; background: var(--copper); }
  .wordmark--back { position: absolute; color: var(--brand-blue); font-size: 13.5px; gap: 7px; }
  .wordmark--back .wordmark__square { width: 14px; height: 14px; background: var(--green); }
  .card--left .wordmark--back { left: 22px; top: 121px; }
  .card--right .wordmark--back { left: 24px; top: 184px; }

  .photo {
    position: absolute;
    left: 49px; top: 46px;
    width: 102px; height: 102px;
    background: linear-gradient(180deg, var(--photo-top) 0%, var(--photo-top) 55%, var(--photo-bottom) 100%);
  }

  .contact { position: absolute; left: 205px; top: 42px; color: var(--ink); }
  .contact__name { font-size: 16px; font-weight: 600; letter-spacing: 2.4px; color: var(--green); line-height: 1; }
  .contact__title { font-size: 12.5px; font-style: italic; color: var(--muted); margin-top: 6px; letter-spacing: 0.3px; }
  .contact__line { font-size: 12.5px; line-height: 19px; letter-spacing: 0.3px; }
  .contact__phone { margin-top: 20px; }
  .contact__web { margin-top: 20px; }
  .contact__license { font-size: 11px; letter-spacing: 0.6px; color: var(--muted); margin-top: 20px; }
</style>
</head>
<body>
  <section class="card card--front card--left">
    <div class="wordmark wordmark--front"><span class="wordmark__square"></span>Silver Meadow Properties</div>
  </section>

  <section class="card card--front card--right">
    <div class="wordmark wordmark--front"><span class="wordmark__square"></span>Silver Meadow Properties</div>
  </section>

  <section class="card card--back card--left">
    <div class="wordmark wordmark--back"><span class="wordmark__square"></span>Silver Meadow Properties</div>
    <div class="contact">
      <p class="contact__name">DANIEL MORROW</p>
      <p class="contact__title">Real Estate Broker, Realtor, MBA</p>
      <p class="contact__line contact__phone">310 555 0147</p>
      <div class="contact__web">
        <p class="contact__line">dan@smprealtyhub.example</p>
        <p class="contact__line">smprealtyhub.example</p>
      </div>
      <p class="contact__license">CA BRE #02719354</p>
    </div>
  </section>

  <section class="card card--back card--right">
    <div class="photo" role="img" aria-label="Headshot photo of the agent in a navy suit against green foliage"></div>
    <div class="wordmark wordmark--back"><span class="wordmark__square"></span>Silver Meadow Properties</div>
    <div class="contact">
      <p class="contact__name">DANIEL MORROW</p>
      <p class="contact__title">Real Estate Broker, Realtor, MBA</p>
      <p class="contact__line contact__phone">310 555 0147</p>
      <div class="contact__web">
        <p class="contact__line">dan@smprealtyhub.example</p>
        <p class="contact__line">smprealtyhub.example</p>
      </div>
      <p class="contact__license">CA BRE #02719354</p>
    </div>
  </section>
</body>
</html>
```